Redesign of Brochure of company services

We need a redesign a brochure. All of the content on the existing brochure correct, but the design we are not pleased with it. I will provide the previous brochure. Quiet Harbor Fields is Angolan company that provides multiple service ranging providing fruits, vegetables, fisheries, and meat to multiple industries in angola. Quiet Harbor Fields seeks to start delivering or providing their service to home owners looking for fresh products. We want a brochure design that covers all of these aspects.

Target Market(s)

Home owners, middle and upper age mothers, middle and upper class

Industry/Entity Type

Retail

Requirements
Must have
• Logo of the company and the content info
Nice to have
• It's up to you

```html
<!DOCTYPE html>
<html lang="pt">
<head>
<meta charset="utf-8">
<title>Quiet Harbor Fields — Brochura</title>
<link href="https://fonts.googleapis.com/css2?family=Lato:wght@400;700;900&family=Lora:ital@1&display=swap" rel="stylesheet">
<style>
:root{
  --olive:#b0b322;
  --forest:#4d5e27;
  --cream:#eae8d7;
  --ink:#4a5a22;
  --orange:#d2490f;
  --body:#2c2c22;
  --label:#c9c9c9;
}
*{margin:0;padding:0;box-sizing:border-box}
html,body{width:937px;height:1200px;overflow:hidden;background:#fff}
body{position:relative;font-family:'Lato',sans-serif;color:var(--body)}
.view-label{position:absolute;font-family:'Lato',sans-serif;font-weight:900;font-size:28px;color:var(--label)}
.spread{position:absolute;width:730px;height:514px;background:var(--cream);box-shadow:0 12px 24px rgba(0,0,0,.28);overflow:hidden}
.spread--inside{left:102px;top:71px}
.spread--outside{left:104px;top:633px}
.top-band{position:absolute;left:0;top:0;width:100%;height:20px;background:var(--olive)}
.base-band{position:absolute;left:0;top:375px;width:100%;height:139px;background:var(--forest)}
.panel{position:absolute;top:0;height:100%}
.panel + .panel{box-shadow:inset 8px 0 12px -8px rgba(0,0,0,.18)}
.band-title{position:absolute;top:3px;font-weight:900;font-size:14px;letter-spacing:5px;color:var(--forest)}
.photo{position:absolute;border-radius:4px}
.section-title{position:absolute;font-weight:700;font-size:12px;letter-spacing:4px;line-height:21px;color:var(--ink)}
.body-text{position:absolute;font-size:8.6px;line-height:11.4px;color:var(--body)}
.quote{position:absolute;font-family:'Lora',serif;font-style:italic;font-size:12px;line-height:15px;color:var(--olive)}
.light{color:#fff}
.small-white{position:absolute;font-size:8.6px;line-height:12px;color:#f2f2e8}
.sub-title{position:absolute;font-weight:700;font-size:11.5px;letter-spacing:1.5px;color:#fff}
.phone-chip{position:absolute;background:var(--olive);color:#fff;font-weight:700;font-size:11.5px;letter-spacing:1.3px;padding:3px 6px}
.lead-orange{position:absolute;font-weight:700;font-size:11.5px;line-height:14.5px;color:var(--orange)}
.steps{position:absolute;list-style:none;font-size:11.5px;line-height:19.5px;color:var(--ink)}
.slogan{position:absolute;font-family:'Lora',serif;font-style:italic;color:var(--ink)}
.slogan span{display:block}
.stamp{position:absolute}
.cta-box{position:absolute;background:var(--orange);color:#fff;font-weight:700;font-size:10.5px;line-height:14.5px;padding:14px 14px}
.service-list{position:absolute;list-style:none;font-weight:700;font-size:12px;letter-spacing:4.5px;line-height:29.5px;color:var(--ink)}
.brand-name{position:absolute;font-weight:400;font-size:21px;color:#fff;white-space:nowrap}
.brand-values{position:absolute;list-style:none;font-weight:700;font-size:11.5px;letter-spacing:4.5px;line-height:20.5px;color:var(--olive)}
</style>
</head>
<body>

<div class="view-label" style="left:424px;top:24px">open</div>

<section class="spread spread--inside">
  <div class="top-band"></div>
  <div class="base-band"></div>

  <article class="panel" style="left:0;width:249px">
    <h2 class="band-title" style="left:40px">QUALIDADE</h2>
    <div class="photo" role="img" aria-label="Cesto com hortaliças e frutas frescas" style="left:36px;top:48px;width:172px;height:126px;border-radius:50%;background:radial-gradient(circle,#c9382a 0%,#d9892d 45%,#6d8a2c 75%,rgba(234,232,215,0) 100%)"></div>
    <h3 class="section-title" style="left:41px;top:188px">HORTALIÇAS<br>E FRUTAS</h3>
    <p class="body-text" style="left:42px;top:245px;width:180px">Fornecemos as mais variadas hortaliças, incluindo batata rena, batata doce, alface, abóbora, couve lombarda, couve repolho, couve repolho roxa,cebola, beterraba, beringela, courgette, nabo, feijão verde e milho.</p>
    <div class="photo" role="img" aria-label="Retrato da gerente" style="left:91px;top:330px;width:58px;height:58px;border-radius:50%;background:linear-gradient(160deg,#8a5a44,#3e2a22)"></div>
    <p class="quote" style="left:42px;top:392px;width:190px">A nossa missão é aproximar os&nbsp; produtores nacionais dos seus clientes finais, garantindo qualidade e consistência.</p>
    <p class="small-white" style="left:43px;top:455px">Lúcia Andrade, Gerente</p>
  </article>

  <article class="panel" style="left:249px;width:243px">
    <h2 class="band-title" style="left:25px">RAPIDEZ</h2>
    <div class="photo" role="img" aria-label="Cortes de carne fresca sobre tábua de madeira" style="left:21px;top:54px;width:194px;height:118px;background:linear-gradient(135deg,#c8504f,#a63a3a 55%,#c88a52)"></div>
    <h3 class="section-title" style="left:27px;top:189px">CARNES</h3>
    <p class="body-text" style="left:28px;top:225px;width:160px">Distribuimos carne fresca de gado ovino, caprino, bovino e suíno e apostamos em produtos de elevada qualidade que nos permitam manter padrões constantes de qualidade dos produtos e dos serviços por nós prestados.</p>
    <svg class="stamp" style="left:82px;top:318px" width="134" height="70" viewBox="0 0 134 70" aria-hidden="true"><rect x="10" y="14" width="114" height="42" fill="none" stroke="#d2490f" stroke-width="3" transform="rotate(-12 67 35)"/></svg>
    <h4 class="sub-title" style="left:29px;top:437px">Produtos nacionais</h4>
    <p class="small-white" style="left:29px;top:455px;font-size:9.5px">Vendemos apenas produtos<br>nacionais de qualidade controlada</p>
  </article>

  <article class="panel" style="left:492px;width:238px">
    <h2 class="band-title" style="left:37px">SATISFAÇÃO</h2>
    <div class="photo" role="img" aria-label="Peixes e mariscos frescos" style="left:20px;top:50px;width:193px;height:113px;background:linear-gradient(160deg,#8a9098,#c9ccd0 50%,#d98a7a)"></div>
    <h3 class="section-title" style="left:35px;top:188px">PEIXES<br>E MARISCOS</h3>
    <p class="body-text" style="left:35px;top:245px;width:180px">Dispomos de uma vasta gama de peixes e mariscos incluindo pescada, salmão, bacalhau, atum, sardinha, carapau, linguado, camarão, lagostim, gambas, entre outros. Fornecemos o peixe e marisco sempre frescos.</p>
    <svg class="stamp" style="left:54px;top:328px" width="60" height="60" viewBox="0 0 60 60" aria-hidden="true"><circle cx="30" cy="30" r="27" fill="none" stroke="#d2490f" stroke-width="3"/></svg>
    <div class="phone-chip" style="left:38px;top:414px">+244 900 000 123</div>
    <h4 class="sub-title" style="left:38px;top:450px">Estamos abertos 24/7</h4>
    <p class="small-white" style="left:38px;top:473px;font-weight:700;letter-spacing:.8px;font-size:9.5px">lucia.andrade@quietharbor.ao</p>
  </article>
</section>

<section class="spread spread--outside">
  <div class="top-band"></div>
  <div class="base-band"></div>

  <article class="panel" style="left:0;width:247px">
    <p class="lead-orange" style="left:29px;top:61px">Trazemos frescos da<br>melhor qualidade a bom preço<br>direitinho à&nbsp; sua porta.</p>
    <h3 class="section-title" style="left:31px;top:117px">CONFIE EM<br>QUALIDADEM</h3>
    <p class="body-text" style="left:31px;top:168px;width:175px">A qualidade de todos os frescos distribuídos por nós é verificada para que apenas os produtos aprovados chegem até si.</p>
    <ol class="steps" style="left:31px;top:222px">
      <li>1. Encomende por telefone</li>
      <li>2. Pague no banco</li>
      <li>3. Receba os seus frescos</li>
    </ol>
    <p class="lead-orange" style="left:31px;top:290px">Fazemos Descontos</p>
    <p class="body-text" style="left:31px;top:305px;width:80px">Fazemos descontos a clientes com contratos de fornecimento contínuo.</p>
    <div class="photo" role="img" aria-label="Tomates maduros vermelhos e amarelos" style="left:0;top:374px;width:240px;height:140px;border-radius:0;background:linear-gradient(135deg,#9a1e12,#d23a1d 45%,#e7a62a 80%,#c23018)"></div>
    <div style="position:absolute;left:107px;top:314px;width:108px;height:108px;border-radius:50%;background:var(--olive)"></div>
    <p class="slogan light" style="left:118px;top:338px;font-size:14.5px;line-height:20px"><span>Qualidade.</span><span style="padding-left:16px">Rapidez.</span><span>Satisfação!</span></p>
    <p class="sub-title" style="left:31px;top:426px;letter-spacing:1.6px">Manuseamos com cuidado</p>
    <p class="sub-title" style="left:31px;top:449px;letter-spacing:1.6px">+244 900 000 123</p>
  </article>

  <article class="panel" style="left:247px;width:243px">
    <svg class="stamp" style="left:51px;top:8px" width="60" height="60" viewBox="0 0 60 60" aria-hidden="true"><circle cx="30" cy="30" r="27" fill="none" stroke="#4a5a22" stroke-width="3"/></svg>
    <p class="slogan" style="left:46px;top:68px;font-size:25px;line-height:31px"><span>Qualidade.</span><span style="padding-left:25px">Rapidez.</span><span>Satisfação!</span></p>
    <div class="photo" role="img" aria-label="Produtor com cesto e gado no campo" style="left:35px;top:227px;width:158px;height:78px;border-radius:0;background:linear-gradient(90deg,#3f4a22,#6a6a3a 50%,#8fa1b8)"></div>
    <div class="photo" role="img" aria-label="Abóboras e cabaças" style="left:190px;top:285px;width:75px;height:90px;border-radius:40% 40% 0 0;background:linear-gradient(160deg,#e07a2a,#c8a23a)"></div>
    <p class="cta-box" style="left:35px;top:305px;width:158px;height:90px">Se for produtor e deseja comercializar os seus produtos de forma segura, contacte-nos hoje!</p>
    <h4 class="sub-title" style="left:35px;top:414px;color:var(--olive);font-weight:400;letter-spacing:2px">QUIET HARBOR FIELDS CORP</h4>
    <p class="small-white" style="left:35px;top:437px;font-size:9.5px">Rua das Acácias, Luanda, Angola<br>+244 900 000 123<br>lucia.andrade@quietharbor.ao</p>
  </article>

  <article class="panel" style="left:490px;width:240px">
    <p class="lead-orange" style="left:58px;top:62px">Levamos produtos<br>frescos Nacionais</p>
    <p class="lead-orange" style="left:35px;top:87px;font-size:28px;line-height:32px">à sua porta</p>
    <ul class="service-list" style="left:58px;top:137px">
      <li>HORTALIÇAS</li>
      <li>FRUTAS</li>
      <li>CARNES</li>
      <li>PEIXES</li>
      <li>MARISCOS</li>
    </ul>
    <p class="brand-name" style="left:34px;top:397px">Quiet Harbor Fields</p>
    <ul class="brand-values" style="left:57px;top:436px">
      <li>QUALIDADE</li>
      <li>RAPIDEZ</li>
      <li>SATISFAÇÃO</li>
    </ul>
  </article>
</section>

<div class="view-label" style="left:409px;top:1152px">back</div>
<div class="view-label" style="left:646px;top:1152px">front</div>

</body>
</html>
```